Velorix Flyer

PROJECT: Digital Flyer for VeloRix

Format
1920 × 1080 px (landscape, optimized for presentations and email)
Deliverables
• PDF
• PNG

About VeloRix
VeloRix is a Dutch B2B software company providing a unified CRM and customer journey platform. We help businesses manage the entire customer lifecycle — from first contact to loyal customer — by centralizing all touchpoints in one system.
What sets us apart:
Extreme ease of use. The system is self-guiding, shows only what's relevant per employee, and requires virtually no training. All channels (email, phone, chat, in-store) come together in one place with automatic task distribution. Built-in AI functions as a smart digital colleague that continuously learns.
Target audience:
Directors and sales managers at B2B companies with multiple customer contact channels.

Goal:
We want to create a flyer that sets us apart from other CRM platform providers. Our aim is to achieve this through simplicity and a professional appearance. The design should reflect our core value: ease of use. The recipient should feel compelled to engage with us — not overwhelmed by information, but intrigued by clarity. Less is more.

Required Text Elements
Headline:
"CRM that adapts to how you work"
Subline:
"Discover how VeloRix simplifies your sales process"
Call-to-action:
"See it in action — book a call"
Contact details:
• hello@velorix.nl
• 023-5718469
• velorix.com

Required Visual Elements
• VeloRix logo (attached)

Design Style
• Modern / Minimalist
• Professional / Business
• Tech / Futuristic
• Clean with plenty of whitespace

Tone of voice:
Clear, positive and customer-focused. Practical and accessible business style aimed at communicating concrete value for users.

Design inspiration — please review these websites:
• orbantal.com
• ravelo.app
• quendo.com
• tirameld.com
• gonwisp.com
What We DON'T Want
• Bold / In-your-face
• Dense / Compact
• Trendy / Experimental
• Childlike / Cheerful
• Playful / Cartoonish
• Busy / Chaotic
Colors
Use the color palette from velorix.com (blues, whites, clean professional tones).
[Exact hex codes used for element on the website:
#344054;
#1a1b1f;
#0254ac
#002249;
#e5edf7;
background-color: #fff; ]
Competitors (for context only — do NOT copy)
• brinvolt.nl
• kelmarin.com
• dortavecrm.com
• wexalunda.com
Budget
$150
Deadline
January 26, 2026

```html
<!DOCTYPE html>
<html lang="en">
<head>
<meta charset="UTF-8">
<title>VeloRix Flyer</title>
<link href="https://fonts.googleapis.com/css2?family=Poppins:wght@400;500;600&display=swap" rel="stylesheet">
<style>
  :root {
    --navy: #1b2150;
    --accent: #4a8ad0;
    --button: #4b88c8;
    --pale: #e5edf7;
    --deep: #0254ac;
    --line: #4a88d0;
    --icon: #1f8de0;
    --white: #ffffff;
  }
  * { margin: 0; padding: 0; box-sizing: border-box; }
  html, body { width: 1200px; height: 675px; overflow: hidden; background: var(--white); }
  .flyer {
    position: relative; width: 1200px; height: 675px; overflow: hidden;
    background: var(--white); font-family: "Poppins", sans-serif; color: var(--navy);
  }
  .backdrop { position: absolute; inset: 0; }
  .brand {
    position: absolute; left: 50px; top: 75px; height: 58px;
    display: flex; align-items: center; gap: 16px;
  }
  .brand-dot { width: 58px; height: 58px; border-radius: 50%; background: var(--navy); flex: none; }
  .brand-name { font-size: 56px; font-weight: 600; letter-spacing: -1.2px; line-height: 1; }
  .headline {
    position: absolute; left: 50px; top: 268px; font-size: 32px; font-weight: 500;
    letter-spacing: -1.2px; line-height: 1.2; white-space: nowrap;
  }
  .headline-lead { font-weight: 600; }
  .subline {
    position: absolute; left: 50px; top: 321px; font-size: 20px; font-weight: 400;
    color: var(--accent); letter-spacing: -0.1px; line-height: 1.3; white-space: nowrap;
  }
  .cta {
    position: absolute; left: 50px; top: 390px; width: 381px; height: 59px;
    background: var(--button); color: var(--white); border-radius: 6px;
    display: flex; align-items: center; justify-content: center;
    font-size: 24px; font-weight: 500; letter-spacing: -0.3px;
    box-shadow: 0 10px 22px rgba(75, 136, 200, 0.25); text-decoration: none;
  }
  .product-view {
    position: absolute; left: 643px; top: 187px; width: 453px; height: 319px;
    border-radius: 12px 12px 4px 4px;
    background: linear-gradient(180deg, #2a2c33 0%, #eef2f8 5%, #f5f8fc 60%, #dfe8f1 100%);
  }
  .contacts { position: absolute; left: 0; top: 567px; width: 1200px; height: 73px; }
  .contact {
    position: absolute; top: 0; height: 73px; display: flex; align-items: center; gap: 10px;
    font-size: 24px; font-weight: 500; color: var(--navy); white-space: nowrap;
  }
  .contact svg { width: 27px; height: 27px; flex: none; }
  .contact-email { left: 50px; }
  .contact-phone { left: 540px; }
  .contact-web { left: 948px; }
  .divider { position: absolute; top: 0; width: 2px; height: 73px; background: var(--line); }
  .divider-one { left: 417px; }
  .divider-two { left: 828px; }
</style>
</head>
<body>
<div class="flyer">
  <svg class="backdrop" width="1200" height="675" viewBox="0 0 1200 675" aria-hidden="true">
    <polygon points="825,145 970,0 1200,0 1200,600 1060,460" fill="var(--pale)" opacity="0.8"/>
    <polygon points="1096,259 1200,154 1200,453" fill="#2a62a8"/>
    <polygon points="1110,262 1200,172 1200,300" fill="#1f4f95"/>
    <polyline points="1200,7 1046,160 1200,315" fill="none" stroke="var(--line)" stroke-width="3"/>
    <line x1="1046" y1="160" x2="1200" y2="315" stroke="#8fb4de" stroke-width="1.5"/>
  </svg>

  <div class="brand">
    <span class="brand-dot"></span>
    <span class="brand-name">VeloRix</span>
  </div>

  <h1 class="headline"><span class="headline-lead">CRM</span> that adapts to how you work</h1>
  <p class="subline">Discover how VeloRix simplifies your sales process.</p>
  <a class="cta" href="#">See it in action - book a call</a>

  <div class="product-view" role="img" aria-label="Laptop showing the VeloRix CRM contacts board with New, Potential, Relation and Other columns"></div>

  <div class="contacts">
    <div class="contact contact-email">
      <svg viewBox="0 0 28 28" aria-hidden="true"><circle cx="14" cy="14" r="14" fill="var(--icon)"/><rect x="7.5" y="9.5" width="13" height="9.5" rx="1.5" fill="none" stroke="#fff" stroke-width="1.8"/><polyline points="8,10.5 14,15 20,10.5" fill="none" stroke="#fff" stroke-width="1.8"/></svg>
      <span>hello@velorix.nl</span>
    </div>
    <span class="divider divider-one"></span>
    <div class="contact contact-phone">
      <svg viewBox="0 0 28 28" aria-hidden="true"><circle cx="14" cy="14" r="14" fill="var(--icon)"/><rect x="9.5" y="6.5" width="9" height="15" rx="1.8" fill="none" stroke="#fff" stroke-width="1.8"/><line x1="12.5" y1="18.5" x2="15.5" y2="18.5" stroke="#fff" stroke-width="1.6"/></svg>
      <span>023-5718469</span>
    </div>
    <span class="divider divider-two"></span>
    <div class="contact contact-web">
      <svg viewBox="0 0 28 28" aria-hidden="true"><circle cx="14" cy="14" r="14" fill="var(--icon)"/><circle cx="14" cy="14" r="7.5" fill="none" stroke="#fff" stroke-width="1.6"/><ellipse cx="14" cy="14" rx="3.3" ry="7.5" fill="none" stroke="#fff" stroke-width="1.4"/><line x1="6.5" y1="14" x2="21.5" y2="14" stroke="#fff" stroke-width="1.4"/></svg>
      <span>velorix.com</span>
    </div>
  </div>
</div>
</body>
</html>
```